Velbrook App Homepage Design making customers feel in control of their spend

Hi,
We need a App Homepage design with a UI similar to the attached mock up on an Quillo 4. The app is intended to put customers in control of their usage and spend on their fixed phone, broadband, mobile, gas and electricity.

Please fee free to propose improvements to the background images, icons, colours, etc.

Any questions please let me know.

Thanks
Tomasz

Target Market(s)

Consumer customers

Industry/Entity Type

Internet

Font styles to use
Sans Serif

Colors
3276b5
0255a3
85acd3
cfdeed
ffffff

Requirements
Must have
• Content in line with the guidelines in the attached mock up

```html
<!DOCTYPE html>
<html lang="en">
<head>
<meta charset="utf-8">
<title>Velbrook – Home</title>
<link rel="stylesheet" href="https://fonts.googleapis.com/css2?family=Josefin+Sans:wght@300;400;600;700&family=Roboto:wght@400&display=swap">
<style>
  :root{
    --status-bg:#150a2e;
    --header-bg:#2a1450;
    --greet-bg:#24113f;
    --main-top:#24104a;
    --main-bottom:#140c3a;
    --footer-bg:#2b1450;
    --text:#ffffff;
    --text-muted:#b9aed0;
    --brand:#3d7fe0;
    --accent:#c8ea10;
    --pill:#4a3570;
    --pill-text:#a497c0;
    --mobile:#ec1c5c;
    --calls:#ff8a00;
    --gas:#c8ea10;
    --electricity:#07a023;
    --fiber:#4b0f8f;
  }
  *{margin:0;padding:0;box-sizing:border-box}
  html,body{width:782px;height:1200px;overflow:hidden;background:var(--status-bg)}
  .screen{position:relative;width:782px;height:1200px;font-family:"Josefin Sans",sans-serif;color:var(--text);overflow:hidden}

  .status-bar{position:absolute;top:0;left:0;width:100%;height:44px;background:var(--status-bg);font-family:"Roboto",sans-serif;font-size:22px}
  .status-bar .signal{position:absolute;left:20px;top:13px;display:flex;gap:4px;align-items:center}
  .status-bar .dot{width:13px;height:13px;border-radius:50%;background:var(--text)}
  .status-bar .dot.empty{background:none;border:1.5px solid var(--text)}
  .status-bar .wifi{position:absolute;left:118px;top:10px}
  .status-bar .time{position:absolute;left:0;right:0;top:10px;text-align:center}
  .status-bar .battery-level{position:absolute;right:86px;top:10px}
  .status-bar .battery{position:absolute;right:14px;top:12px;width:56px;height:22px;border:2px solid var(--text);border-radius:4px;padding:2px}
  .status-bar .battery::before{content:"";display:block;width:100%;height:100%;background:var(--text);border-radius:2px}
  .status-bar .battery::after{content:"";position:absolute;right:-6px;top:6px;width:3px;height:7px;background:var(--text);border-radius:0 2px 2px 0}

  .app-header{position:absolute;top:44px;left:0;width:100%;height:116px;background:linear-gradient(90deg,#2a1450,#331a5a)}
  .brand{position:absolute;left:50px;top:38px;display:flex;align-items:center;gap:14px}
  .brand-mark{width:40px;height:40px;border-radius:50%;background:var(--brand)}
  .brand-name{font-size:33px;font-weight:400;color:var(--brand)}
  .menu-icon{position:absolute;right:36px;top:50px;width:40px;display:flex;flex-direction:column;gap:5px}
  .menu-icon span{height:3px;background:var(--text);border-radius:2px}

  .greeting{position:absolute;top:160px;left:0;width:100%;height:144px;background:var(--greet-bg);text-align:center}
  .greeting h1{font-weight:300;font-size:44px;letter-spacing:1px;margin-top:30px}
  .greeting p{font-weight:700;font-size:20px;letter-spacing:.5px;margin-top:20px}

  .dashboard{position:absolute;top:304px;left:0;width:100%;height:754px;background:linear-gradient(160deg,var(--main-top),var(--main-bottom) 80%)}
  .support-pill{position:absolute;left:322px;top:70px;width:138px;height:68px;border-radius:34px;background:var(--pill);box-shadow:0 0 0 5px rgba(74,53,112,.45);text-align:center;color:var(--pill-text);font-weight:700;font-size:20px;line-height:24px;padding-top:11px;letter-spacing:1px}

  .usage-chart{position:absolute;left:221px;top:271px;width:340px;height:340px}
  .chart-total{position:absolute;left:221px;top:396px;width:340px;text-align:center}
  .chart-total .label{font-weight:700;font-size:20px;letter-spacing:.5px;margin-left:-26px}
  .chart-total .amount{font-weight:300;font-size:40px;margin-top:4px}

  .legend-item{position:absolute;display:flex;align-items:center;gap:18px;font-weight:700;font-size:20px;letter-spacing:.5px}
  .legend-item i{display:block;width:32px;height:32px;border-radius:50%}
  .legend-mobile{left:86px;top:286px}
  .legend-calls{left:520px;top:272px}
  .legend-gas{left:604px;top:422px}
  .legend-fiber{left:88px;top:551px}
  .legend-electricity{left:502px;top:605px}

  .bill-summary{position:absolute;top:1058px;left:0;width:100%;height:142px;background:var(--footer-bg);text-align:center}
  .bill-summary .latest{font-weight:700;font-size:27px;margin-top:44px}
  .bill-summary .latest em{font-style:normal;color:var(--accent)}
  .bill-summary .renews{font-weight:600;font-size:18px;color:var(--text-muted);letter-spacing:.5px;margin-top:14px}
</style>
</head>
<body>
<div class="screen">
  <div class="status-bar">
    <div class="signal"><span class="dot"></span><span class="dot"></span><span class="dot"></span><span class="dot"></span><span class="dot empty"></span></div>
    <svg class="wifi" width="28" height="22" viewBox="0 0 28 22" aria-hidden="true">
      <path d="M2 8a17 17 0 0 1 24 0M6 12a11 11 0 0 1 16 0M10 16a5 5 0 0 1 8 0" fill="none" stroke="#fff" stroke-width="2.5" stroke-linecap="round"/>
      <circle cx="14" cy="19.5" r="2" fill="#fff"/>
    </svg>
    <div class="time">2:56 PM</div>
    <div class="battery-level">100%</div>
    <div class="battery"></div>
  </div>

  <header class="app-header">
    <div class="brand"><span class="brand-mark"></span><span class="brand-name">Velbrook</span></div>
    <div class="menu-icon"><span></span><span></span><span></span></div>
  </header>

  <section class="greeting">
    <h1>Good Morning Marla</h1>
    <p>WELCOME TO VELBROOK</p>
  </section>

  <main class="dashboard">
    <div class="support-pill">24\7<br>SUPPORT</div>

    <svg class="usage-chart" viewBox="-170 -170 340 340" role="img" aria-label="Spending breakdown by service">
      <g fill="none" stroke-width="64">
        <path d="M0 -138 A138 138 0 0 1 136.7 -19.2" stroke="var(--calls)"/>
        <path d="M136.7 -19.2 A138 138 0 0 1 137 16.8" stroke="var(--gas)"/>
        <path d="M137 16.8 A138 138 0 0 1 -33.4 133.9" stroke="var(--electricity)"/>
        <path d="M-33.4 133.9 A138 138 0 0 1 -137 -16.8" stroke="var(--fiber)"/>
        <path d="M-137 -16.8 A138 138 0 0 1 0 -138" stroke="var(--mobile)"/>
      </g>
    </svg>
    <div class="chart-total">
      <div class="label">TOTAL</div>
      <div class="amount">£68.39</div>
    </div>

    <div class="legend-item legend-mobile">MOBILE <i style="background:var(--mobile)"></i></div>
    <div class="legend-item legend-calls"><i style="background:var(--calls)"></i> CALLS</div>
    <div class="legend-item legend-gas"><i style="background:var(--gas)"></i> GAS</div>
    <div class="legend-item legend-fiber">FIBER <i style="background:var(--fiber)"></i></div>
    <div class="legend-item legend-electricity"><i style="background:var(--electricity)"></i> ELECTRICITY</div>
  </main>

  <footer class="bill-summary">
    <div class="latest">LATEST BILL <em>£45.75</em> ON <em>09.12.2016</em></div>
    <div class="renews">ALLOWANCE RENEWS IN 18 DAYS</div>
  </footer>
</div>
</body>
</html>
```